Larkmoor Capital - Financial Planning Solutions

Larkmoor Capital is a financial planning business in Melbourne, Australia. We cater to all kinds of clients from high net worth individuals to young people just starting a career. We need a chart, which will be included in client pitches, presentations and on our website, that conveys the various areas that we are able to provide client solutions.
We have attached three rudimentary interpretations of what we're talking about, one of which includes our logo. With each area of advice we have included a brief description of what it is. The different areas are not necessarily linked, so it's not a circular process but there is a logical progression to them: clients can ask us to get involved with any of the steps.
We are pretty open to suggestions as to the best presentation but are quite interested in an infographics approach.
You can check out our website at www.larkmoorcapital.com.au to see a bit about us, but please be aware that we are changing our investment philosophy and the tone of the website to a broader appeal.
Cheers, Oliver

```html
<!DOCTYPE html>
<html lang="en">
<head>
<meta charset="utf-8">
<title>Larkmoor Capital – Presentation</title>
<link href="https://fonts.googleapis.com/css2?family=Roboto+Condensed:wght@400;700&family=Roboto:wght@300;400;500&display=swap" rel="stylesheet">
<style>
  :root{
    --board:#222222;
    --slide-light:#f1f1f1;
    --slide-mid:#e3e3e3;
    --bronze:#6e5c3e;
    --bronze-dark:#3f3222;
    --ring:#6d6d6d;
    --ink:#2b2b2b;
    --muted:#7a7a7a;
    --footer:#2e2f33;
    --footer-dark:#26272a;
    --white:#ffffff;
  }
  *{margin:0;padding:0;box-sizing:border-box}
  html,body{width:1200px;height:1200px;overflow:hidden;background:var(--board)}
  body{position:relative;font-family:'Roboto',sans-serif;color:var(--white)}

  .page-label{position:absolute;left:96px;font-family:'Roboto',sans-serif;font-size:25px;font-weight:400;color:var(--white)}
  .page-label.p2{top:260px}
  .page-label.p3{top:780px}

  .slide{position:absolute;left:240px;width:720px;height:450px;overflow:hidden;
    background:radial-gradient(ellipse at 50% 40%,var(--slide-light) 0%,var(--slide-mid) 100%)}
  .slide.s2{top:59px}
  .slide.s3{top:570px}

  .slide-footer{position:absolute;left:0;top:410px;width:720px;height:40px;background:var(--footer);border-top:2px solid var(--bronze)}
  .footer-brand{position:absolute;left:68px;top:9px;font-family:'Roboto',sans-serif;font-weight:400;font-size:12px;letter-spacing:3px;line-height:1.1;color:var(--white);text-align:center}
  .footer-sep{position:absolute;left:212px;top:6px;width:1px;height:28px;background:#3d3e43}
  .footer-date{position:absolute;left:226px;top:15px;font-size:8px;color:#6b6c70;font-weight:300}
  .pager{position:absolute;left:542px;top:0;width:63px;height:38px;background:var(--footer-dark)}
  .pager .lbl{position:absolute;left:6px;top:18px;font-size:9px;color:#777;font-weight:300}
  .pager .num{position:absolute;left:33px;top:6px;font-size:20px;color:#8d8e92;font-weight:300}
  .nav-btn{position:absolute;top:11px;width:16px;height:16px}
  .nav-btn.prev{left:518px}
  .nav-btn.next{left:614px}

  .diagram{position:absolute;left:0;top:0}

  .s3 .title{position:absolute;left:64px;top:36px;font-family:'Roboto Condensed',sans-serif;font-weight:700;font-size:24px;color:var(--ink)}
  .artifact{position:absolute;left:70px;top:94px;width:184px;height:228px;
    background:linear-gradient(180deg,#9d8a5f 0%,#6a5a3c 45%,#b5a47e 75%,rgba(220,220,220,0) 100%);
    border-radius:6px;opacity:.55}
  .divider{position:absolute;left:314px;top:102px;width:1px;height:224px;background:#d6d6d6}
  .about-head{position:absolute;left:350px;top:129px;font-family:'Roboto Condensed',sans-serif;font-weight:700;font-size:18px;color:var(--bronze-dark)}
  .definition{position:absolute;left:350px;top:166px;width:280px;font-family:'Roboto Condensed',sans-serif;font-weight:700;font-size:13.5px;line-height:16.5px;color:var(--ink)}
  .definition em{font-style:normal;color:var(--bronze)}
  .about-copy{position:absolute;left:350px;top:242px;width:280px;font-size:10.3px;line-height:13.6px;font-weight:300;color:var(--muted)}
  .about-copy strong{font-weight:400;color:var(--ink)}
  .tabs{position:absolute;left:212px;top:378px;display:flex;gap:5px}
  .tab{width:78px;height:15px;background:var(--bronze);color:var(--white);font-size:7px;letter-spacing:1.2px;line-height:15px;text-align:center;font-weight:500}

  .rule{position:absolute;left:38px;top:1068px;width:1108px;height:1px;background:#444}
  .board-brand{position:absolute;left:104px;top:1112px;font-family:'Roboto',sans-serif;font-weight:400;font-size:22px;letter-spacing:6px;line-height:1.15;color:var(--white);text-align:center}
  .board-caption{position:absolute;left:728px;top:1112px;font-size:18px;font-weight:400;color:var(--white)}
</style>
</head>
<body>

<div class="page-label p2">Page 02</div>
<div class="page-label p3">Page 03</div>

<section class="slide s2">
  <svg class="diagram" width="720" height="410" viewBox="0 0 900 512">
    <circle cx="569" cy="268" r="190" fill="none" stroke="var(--ring)" stroke-width="7"/>
    <g font-family="Roboto Condensed, sans-serif" text-anchor="middle" fill="#fff">
      <text x="80" y="262" text-anchor="start" fill="#2b2b2b" font-weight="700" font-size="14">FINANCIAL PLANNING SOLUTIONS</text>
      <text x="80" y="281" text-anchor="start" fill="#777" font-size="12">Larkmoor Capital is able to help at any stage</text>

      <circle cx="569" cy="253" r="78" fill="var(--bronze-dark)"/>
      <circle cx="569" cy="253" r="72" fill="var(--bronze)"/>
      <text font-weight="700" font-size="18"><tspan x="569" y="236">LARKMOOR</tspan><tspan x="569" y="258">CAPITAL</tspan><tspan x="569" y="280">SOLUTIONS</tspan></text>

      <g stroke="#efefef" stroke-width="8" fill="var(--bronze)">
        <circle cx="567" cy="79" r="52"/>
        <circle cx="720" cy="149" r="52"/>
        <circle cx="764" cy="302" r="52"/>
        <circle cx="659" cy="426" r="52"/>
        <circle cx="488" cy="426" r="52"/>
        <circle cx="375" cy="302" r="52"/>
        <circle cx="413" cy="149" r="52"/>
      </g>

      <text x="567" y="64" font-weight="700" font-size="12">Tax Advice</text>
      <text font-family="Roboto, sans-serif" font-size="8.5"><tspan x="567" y="89">Maximise after</tspan><tspan x="567" y="100">tax income</tspan></text>

      <text font-weight="700" font-size="12"><tspan x="720" y="125">Financial</tspan><tspan x="720" y="140">Planning</tspan></text>
      <text font-family="Roboto, sans-serif" font-size="8.5"><tspan x="720" y="159">A strategy for</tspan><tspan x="720" y="170">your financial</tspan><tspan x="720" y="181">future</tspan></text>

      <text x="764" y="285" font-weight="700" font-size="12">Debt</text>
      <text font-family="Roboto, sans-serif" font-size="8.5"><tspan x="764" y="302">To fund the</tspan><tspan x="764" y="313">purchase of</tspan><tspan x="764" y="324">assets</tspan></text>

      <text x="659" y="410" font-weight="700" font-size="12">Super</text>
      <text font-family="Roboto, sans-serif" font-size="8.5"><tspan x="659" y="435">One of your largest</tspan><tspan x="659" y="446">assets</tspan></text>

      <text x="488" y="410" font-weight="700" font-size="12">Investment</text>
      <text font-family="Roboto, sans-serif" font-size="8.5"><tspan x="488" y="429">S - Optimise</tspan><tspan x="488" y="440">return on your</tspan><tspan x="488" y="451">after tax income</tspan></text>

      <text x="375" y="285" font-weight="700" font-size="12">Insurance</text>
      <text font-family="Roboto, sans-serif" font-size="8.5"><tspan x="375" y="302">Lifestyle protec-</tspan><tspan x="375" y="313">tion for you and</tspan><tspan x="375" y="324">your family</tspan></text>

      <text x="413" y="133" font-weight="700" font-size="12">Estate Planning</text>
      <text font-family="Roboto, sans-serif" font-size="8.5"><tspan x="413" y="152">Ensure your</tspan><tspan x="413" y="163">assets are dealt</tspan><tspan x="413" y="174">with as you want</tspan></text>
    </g>
  </svg>

  <footer class="slide-footer">
    <div class="footer-brand">LARKMOOR<br>CAPITAL</div>
    <div class="footer-sep"></div>
    <div class="footer-date">DATE: AUGUSTUST 28, 2013</div>
    <svg class="nav-btn prev" viewBox="0 0 16 16"><circle cx="8" cy="8" r="8" fill="#fff"/><path d="M9.5 4.5 6 8l3.5 3.5" fill="none" stroke="#2e2f33" stroke-width="2"/></svg>
    <div class="pager"><span class="lbl">PAGE</span><span class="num">02</span></div>
    <svg class="nav-btn next" viewBox="0 0 16 16"><circle cx="8" cy="8" r="8" fill="#fff"/><path d="M6.5 4.5 10 8l-3.5 3.5" fill="none" stroke="#2e2f33" stroke-width="2"/></svg>
  </footer>
</section>

<section class="slide s3">
  <h2 class="title">The Larkmoor</h2>
  <div class="artifact" role="img" aria-label="Photograph of an ornate ceremonial sword hilt"></div>
  <div class="divider"></div>
  <h3 class="about-head">About Larkmoor</h3>
  <p class="definition"><em>Larkmoor</em> - a name for the open moor where larks rise at dawn, a place of steady care, watchfulness and trust.</p>
  <p class="about-copy"><strong>Larkmoor Capital</strong> is a boutique, independently owned, financial advisory and wealth management firm. We aim to provide exceptional service to our clients with our comprehensive approach to building, managing and protecting their wealth.</p>
  <nav class="tabs">
    <span class="tab">WHAT WE DO</span>
    <span class="tab">HOW WE DO IT</span>
    <span class="tab">PHILOSOPHY</span>
    <span class="tab">OUR DIRECTORS</span>
  </nav>

  <footer class="slide-footer">
    <div class="footer-brand">LARKMOOR<br>CAPITAL</div>
    <div class="footer-sep"></div>
    <div class="footer-date">DATE: AUGUSTUST 28, 2013</div>
    <svg class="nav-btn prev" viewBox="0 0 16 16"><circle cx="8" cy="8" r="8" fill="#fff"/><path d="M9.5 4.5 6 8l3.5 3.5" fill="none" stroke="#2e2f33" stroke-width="2"/></svg>
    <div class="pager"><span class="lbl">PAGE</span><span class="num">03</span></div>
    <svg class="nav-btn next" viewBox="0 0 16 16"><circle cx="8" cy="8" r="8" fill="#fff"/><path d="M6.5 4.5 10 8l-3.5 3.5" fill="none" stroke="#2e2f33" stroke-width="2"/></svg>
  </footer>
</section>

<div class="rule"></div>
<div class="board-brand">LARKMOOR<br>CAPITAL</div>
<div class="board-caption">POWER POINT PRESENTATION</div>

</body>
</html>
```